National Human Immunology Network Needs a Brochure DesignBrochure Design Project

We need a brochure design for a new Canadian network called VEKO. VEKO stands for "VRSL Cellular Defence Alliance". (VRSL is the Northfield Councils of Medical Inquiry and is the funder of the network).

The VRSL Cellular Defence Alliance (VEKO) is a resource network that facilitates, promotes and enhances research in human immunology and its translation into clinical care and public policy. VEKO is an inclusive National Network with International projections that will act as a coordinating resource for investigators working in different aspects of Human Immunology. As a research network, VEKO will operate as a resource “umbrella” network, facilitating communication between nodes, each with their specialized expertise in human immunology,
collaboration and knowledge exchange.

We have a VEKO logo already designed as well as the text to be used in the brochure. In addition we should include the VRSL logo somewhere on the brochure, but it does need to be front and centre. Thinking that a tri-fold brochure would work best.

Target Market(s)

Researchers, politicians, lay public

Industry/Entity Type

Communication

Requirements
Must have
• Must use logo provided.

```html
<!DOCTYPE html>
<html lang="en">
<head>
<meta charset="utf-8">
<title>VEKO Brochure – Inside Spread</title>
<link rel="stylesheet" href="https://fonts.googleapis.com/css2?family=Alegreya:ital@1&family=Noto+Serif:wght@400&family=Open+Sans:wght@300&display=swap">
<style>
  :root {
    --bg: #e4e4e4;
    --paper: #ffffff;
    --paper-shade: #f1ebeb;
    --red: #c0202b;
    --red-deep: #8e1219;
    --red-mid: #b8333a;
    --ink: #2a2424;
    --ink-soft: #6a6464;
    --rule: #d46a70;
  }
  * { box-sizing: border-box; margin: 0; padding: 0; }
  html, body { width: 1200px; height: 900px; overflow: hidden; }
  body {
    background: var(--bg);
    display: flex;
    align-items: center;
    justify-content: center;
    font-family: "Noto Serif", Georgia, serif;
    color: var(--ink);
  }
  .spread {
    display: flex;
    width: 960px;
    height: 820px;
    box-shadow: 0 10px 30px rgba(0,0,0,.18);
  }
  .panel {
    width: 480px;
    height: 100%;
    padding: 40px 48px;
    position: relative;
    overflow: hidden;
  }
  .panel--left {
    background: linear-gradient(90deg, var(--paper-shade) 0%, var(--paper) 35%, var(--paper) 85%, #f4f0f0 100%);
  }
  .panel--right { background: var(--paper); }
  .section-title {
    font-family: "Alegreya", Georgia, serif;
    font-style: italic;
    font-weight: 400;
    color: var(--red);
    font-size: 38px;
    line-height: 1.1;
    padding-bottom: 8px;
    border-bottom: 2px dotted var(--rule);
    margin-bottom: 16px;
  }
  .section-title--right { text-align: right; }
  .section { margin-bottom: 34px; }
  .aim-list, .deliverable-list, .accomplishment-list { list-style: none; }
  .aim-list li, .accomplishment-list li {
    position: relative;
    padding-left: 22px;
    font-size: 14.5px;
    line-height: 1.35;
    margin-bottom: 10px;
  }
  .aim-list li::before, .accomplishment-list li::before {
    content: "*";
    position: absolute;
    left: 2px; top: -3px;
    color: var(--red);
    font-size: 24px;
    font-family: "Alegreya", Georgia, serif;
  }
  .deliverable-list li {
    position: relative;
    padding-left: 24px;
    font-size: 16px;
    line-height: 1.35;
    margin-bottom: 12px;
  }
  .deliverable-list .num {
    position: absolute;
    left: 0; top: -2px;
    color: var(--red);
    font-family: "Alegreya", Georgia, serif;
    font-style: italic;
    font-size: 20px;
  }
  .intro {
    font-family: "Open Sans", Arial, sans-serif;
    font-weight: 300;
    font-size: 16px;
    line-height: 1.4;
    color: var(--ink-soft);
    margin-bottom: 14px;
    padding-left: 40px;
  }
  .accomplishment-list { padding-left: 20px; }
  .accomplishment-list li { font-size: 15.5px; }
  .leaf-texture {
    position: absolute;
    left: 0; bottom: 0;
    width: 100%;
    height: 320px;
    background: radial-gradient(ellipse at 40% 40%, var(--red-mid) 0%, var(--red) 45%, var(--red-deep) 100%);
  }
  .panel-band {
    position: absolute;
    left: 0; bottom: 0;
    width: 100%;
    height: 14px;
    background: var(--red-deep);
  }
</style>
</head>
<body>
  <main class="spread">
    <section class="panel panel--left">
      <div class="section section--aims">
        <h2 class="section-title">Specific Aims:</h2>
        <ul class="aim-list">
          <li>To be a source of standardized protocols for human immunology research;</li>
          <li>To facilitate access to research material and technologies, and to expedite regulatory processes;</li>
          <li>To engage national and international human immunology stakeholders to promote research in human immunology; and</li>
          <li>To lead the development of activities of knowledge dissemination in human immunology at national and international levels.</li>
        </ul>
      </div>
      <div class="section section--deliverables">
        <h2 class="section-title">Deliverables:</h2>
        <ol class="deliverable-list">
          <li><span class="num">1.</span>To standardize protocols for human sample processing and sharing;</li>
          <li><span class="num">2.</span>To facilitate access to research material and reagents through formalized collaborations;</li>
          <li><span class="num">3.</span>To expedite ethical and biosafety protocols for human immunology research;</li>
          <li><span class="num">4.</span>To organize an Annual International Conference on human infection and immunity;</li>
          <li><span class="num">5.</span>To provide linkage between the Canadian human immunology research community and international organization-based initiatives in human immunology research.</li>
        </ol>
      </div>
    </section>

    <section class="panel panel--right">
      <h2 class="section-title section-title--right">Accomplishments:</h2>
      <p class="intro">In its first year of operation, VEKO has made significant strides in the establishment of the network. Accomplishments to date include:</p>
      <ul class="accomplishment-list">
        <li>Establishment and set-up of the administrative coordinating node</li>
        <li>Launch of the VEKO website</li>
        <li>Face-to-face meeting of the node leaders in December 2011, and regular monthly teleconference meetings</li>
        <li>Organization of a satellite symposium on “Immune Regulatory Mechanisms in Health &amp; Disease” at ORVIS 2012 in Harrowgate in partnership with the Northfield Society of Immunology</li>
        <li>Formation of an External Advisory Board to provide advice and guidance to the network</li>
      </ul>
      <div class="leaf-texture" role="img" aria-label="Close-up photograph of a red leaf with water droplets"></div>
      <div class="panel-band"></div>
    </section>
  </main>
</body>
</html>
```